Letterhead for small civil engineer company

We need bold and modern design for company letterhead in MS word. It needs to have company logo and company info. Somewhere in the upper right part of document needs to be space for "recever" and the documents starts with, example, "SUBJECT: CIVIL ENGINEER LETTERHEAD".

in the bottom part of document needs to be signature and date.

Company info: Vrelon d.o.o., Dravunja 47, Velmir (Općina Stranje), OIB 47392615084, www.vrelon.hr, info@vrelon.hr

Email of document sender needs to be somewhere if document, exapmle xyz@vrelo.hr

Target Market(s)

Civil engineer company and projects

Industry/Entity Type

Civil engineer

Font styles to use
Serif

Colors
F0912C
F2A743
F7CA91
FBE8D2
FDF5EE

Requirements
Must have
• Company logo and company info
Nice to have
• Moder and clean design
Should not have
• Too much details

```html
<!DOCTYPE html>
<html lang="en">
<head>
<meta charset="utf-8">
<title>Vrelon Letterhead</title>
<link href="https://fonts.googleapis.com/css2?family=Poppins:wght@300;400;500;600;700&display=swap" rel="stylesheet">
<style>
  :root {
    --orange: #F0912C;
    --orange-mid: #F2A743;
    --orange-soft: #F7CA91;
    --orange-pale: #FBE8D2;
    --orange-mist: #FDF5EE;
    --ink: #1d1d1d;
    --ink-soft: #3a3a3a;
    --slate: #5f5f5f;
    --backdrop: #cfd5d4;
    --paper: #ffffff;
  }
  * { margin: 0; padding: 0; box-sizing: border-box; }
  html, body {
    width: 1200px; height: 686px; overflow: hidden;
    background: var(--backdrop);
    font-family: "Poppins", sans-serif;
    color: var(--ink);
  }
  .letterhead {
    position: absolute; left: 370px; top: 18px;
    width: 460px; height: 650px;
    background: var(--paper);
    overflow: hidden;
  }
  .corner { position: absolute; }
  .corner--top { right: 0; top: 0; }
  .corner--bottom { left: 0; bottom: 0; }

  .header {
    position: absolute; left: 34px; right: 34px; top: 30px; height: 72px;
    display: flex; justify-content: space-between; align-items: flex-end;
  }
  .brand { display: flex; align-items: center; gap: 8px; }
  .brand__square { width: 22px; height: 22px; border: 1.5px solid var(--slate); }
  .brand__name {
    font-size: 21px; font-weight: 400; letter-spacing: 1.5px;
    color: var(--orange);
  }
  .recipient { text-align: right; }
  .recipient__label { font-size: 13px; font-weight: 600; color: var(--orange); line-height: 1.1; }
  .recipient__name { font-size: 15px; line-height: 1.2; }
  .recipient__name b { font-weight: 700; }
  .recipient__name span { font-weight: 300; }
  .recipient__role { font-size: 7px; font-weight: 500; }

  .rule {
    position: absolute; left: 34px; right: 34px; top: 110px;
    height: 1.5px; background: var(--orange);
  }
  .subject {
    position: absolute; left: 34px; top: 118px;
    font-size: 8.5px; font-weight: 600; letter-spacing: .3px;
  }
  .subject__label { color: var(--orange); }

  .addressee { position: absolute; left: 34px; top: 146px; }
  .addressee__date { font-size: 7.5px; color: var(--ink-soft); }
  .addressee__name { font-size: 16px; line-height: 1.15; }
  .addressee__name b { font-weight: 700; }
  .addressee__name span { font-weight: 300; }
  .addressee__role { font-size: 7px; font-weight: 500; }

  .body-copy {
    position: absolute; left: 34px; right: 60px; top: 212px;
    font-size: 8px; line-height: 1.75; font-weight: 400; color: var(--ink);
  }
  .body-copy p + p { margin-top: 14px; }

  .sign-off { position: absolute; left: 44px; top: 500px; width: 200px; }
  .sign-off__signature {
    width: 160px; height: 48px; border-radius: 24px;
    background: linear-gradient(90deg, var(--orange-pale), var(--orange-mist));
  }
  .sign-off__role { margin-top: 6px; font-size: 7px; }
  .sign-off__date, .sign-off__email { font-size: 8px; font-weight: 600; line-height: 1.4; }

  .contact {
    position: absolute; right: 24px; top: 500px;
    font-size: 8px; font-weight: 500; line-height: 1.55;
    font-style: normal; text-align: right;
  }
  .contact__row { display: flex; justify-content: flex-end; align-items: center; gap: 6px; }
  .contact__row--continued { padding-right: 15px; }
  .contact__icon { width: 9px; height: 9px; flex: none; }
</style>
</head>
<body>
<main class="letterhead">
  <svg class="corner corner--top" width="140" height="60" viewBox="0 0 140 60" aria-hidden="true">
    <polygon points="0,0 140,0 140,60" fill="var(--orange)"/>
  </svg>

  <header class="header">
    <div class="brand">
      <div class="brand__square"></div>
      <div class="brand__name">VRELON</div>
    </div>
    <div class="recipient">
      <div class="recipient__label">Recever</div>
      <div class="recipient__name"><b>Maren</b> <span>Tolvik</span></div>
      <div class="recipient__role">Founder &amp; CEO</div>
    </div>
  </header>

  <div class="rule"></div>
  <div class="subject"><span class="subject__label">SUBJECT:</span> CIVIL ENGINEER LETTERHEAD</div>

  <section class="addressee">
    <div class="addressee__date">August-05-2019</div>
    <div class="addressee__name"><b>Maren</b> <span>Tolvik</span></div>
    <div class="addressee__role">Founder &amp; CEO</div>
  </section>

  <section class="body-copy">
    <p>Lorem ipsum dolor sit amet, consectetuer adipiscing elit, sed diam nonummy nibh euismod tincidunt ut laoreet dolore magna aliquam erat volutpat. Ut wisi enim ad minim veniam, quis nostrud exerci tation ullamcorper suscipit lobortis nisl ut aliquip ex ea commodo consequat. Duis autem vel eum iriure dolor in hendrerit in vulputate velit esse molestie consequat, vel illum dolore eu feugiat nulla facilisis at vero eros et accumsan et iusto odio dignissim qui blandit praesent luptatum zzril delenit augue duis dolore te feugait nulla facilisi.</p>
    <p>Lorem ipsum dolor sit amet, cons ectetuer adipiscing elit, sed diam nonummy nibh euismod tincidunt ut laoreet dolore magna aliquam erat volutpat. Ut wisi enim ad minim veniam, quis nostrud exerci tation ullamcorper suscipit lobortis nisl ut aliquip ex ea commodo consequat.</p>
    <p>Lorem ipsum dolor sit amet, consectetuer adipiscing elit, sed diam nonummy nibh euismod tincidunt ut laoreet dolore magna aliquam erat</p>
  </section>

  <section class="sign-off">
    <div class="sign-off__signature" role="img" aria-label="Handwritten signature of the sender"></div>
    <div class="sign-off__role">Co-Founder</div>
    <div class="sign-off__date">Date: 14/12/2024</div>
    <div class="sign-off__email">xyz@vrelo.hr</div>
  </section>

  <address class="contact">
    <div class="contact__row">OIB 47392615084
      <svg class="contact__icon" viewBox="0 0 10 10" aria-hidden="true"><path d="M2 1l2 2-1 1.2c.6 1.3 1.5 2.2 2.8 2.8L7 6l2 2-1.2 1.2C4.5 9 1 5.5.8 2.2z" fill="var(--orange)"/></svg>
    </div>
    <div class="contact__row">www.vrelon.hr
      <svg class="contact__icon" viewBox="0 0 10 10" aria-hidden="true"><circle cx="5" cy="5" r="4" fill="none" stroke="var(--orange)" stroke-width="1.2"/><path d="M1 5h8M5 1c-2 2.5-2 5.5 0 8M5 1c2 2.5 2 5.5 0 8" fill="none" stroke="var(--orange)" stroke-width=".8"/></svg>
    </div>
    <div class="contact__row">info@vrelon.hr
      <svg class="contact__icon" viewBox="0 0 10 10" aria-hidden="true"><rect x=".8" y="2" width="8.4" height="6" fill="none" stroke="var(--orange)" stroke-width="1.2"/><path d="M1 2.3l4 3 4-3" fill="none" stroke="var(--orange)" stroke-width="1"/></svg>
    </div>
    <div class="contact__row">Vrelon d.o.o., Dravunja 47,
      <svg class="contact__icon" viewBox="0 0 10 10" aria-hidden="true"><path d="M5 9.5S1.8 6 1.8 3.8a3.2 3.2 0 016.4 0C8.2 6 5 9.5 5 9.5z" fill="var(--orange)"/><circle cx="5" cy="3.8" r="1.1" fill="#fff"/></svg>
    </div>
    <div class="contact__row contact__row--continued">Velmir (Općina Stranje)</div>
  </address>

  <svg class="corner corner--bottom" width="180" height="80" viewBox="0 0 180 80" aria-hidden="true">
    <polygon points="0,0 180,80 0,80" fill="var(--slate)"/>
    <polygon points="0,24 130,80 0,80" fill="var(--orange)"/>
  </svg>
</main>
</body>
</html>
```